Modern CNC Machining Facility in Need of Web Site Improvement

Brightmoor Fabrication and Tooling, LLC is in need of a web site update. We need to highlight both product sales and our manufacturing services offered. We have recently started offering online product sales and need a better ecommerce platform for our customers. We would like the design winner to be able to freelance the project to a fully functioning webpage.
www.brightmoorfab.example
What we like about our current web site:
Black and red highlight colors
Gear and caliper logo
USMC Veteran owned business
What we don't like about our current web site:
Unorganized
Doesn't stand out
Looks like it was made in 1995
Online Product sales are awkward

```html
<!DOCTYPE html>
<html lang="en">
<head>
<meta charset="utf-8">
<title>Brightmoor Fabrication and Tooling, LLC</title>
<link rel="stylesheet" href="https://fonts.googleapis.com/css2?family=Arimo:wght@400;700&family=Tinos&display=swap">
<style>
:root{
  --red:#a0151a;
  --red-btn:#a8161c;
  --black:#161616;
  --nav:#2b2b2b;
  --hero-blue:#2d3868;
  --hero-steel:#8d929c;
  --white:#ffffff;
  --text:#d8d8d8;
  --muted:#8a8a8a;
  --rule:#3a3a3a;
  --panel:#e4e4e6;
  --social:#1e1e1e;
}
*{margin:0;padding:0;box-sizing:border-box}
html,body{width:1200px;height:1198px;overflow:hidden;background:var(--black)}
body{position:relative;font-family:"Arimo",Arial,sans-serif;color:var(--text)}
.abs{position:absolute}

.hero{left:0;top:0;width:1200px;height:328px;background:linear-gradient(100deg,#3b4466 0%,#6d727f 22%,var(--hero-steel) 40%,#5a6284 62%,var(--hero-blue) 80%,#3a4675 100%)}
.brand-panel{left:274px;top:12px;width:681px;height:62px;background:var(--panel);display:flex;align-items:center;padding-left:169px;gap:20px}
.brand-mark{width:40px;height:40px;border-radius:50%;background:var(--red);flex:none}
.brand-name{color:var(--red);font-size:15px;font-weight:700;font-variant:small-caps;letter-spacing:.3px}
.brand-tag{font-family:"Tinos",serif;font-size:10px;color:#333;margin-top:5px}
.hero-rule{top:191px;height:1px;background:rgba(255,255,255,.5)}
.hero-dot{left:609px;top:183px;width:17px;height:17px;border-radius:50%;background:#d8d8d8}
.tagline{left:0;top:239px;width:1200px;text-align:center;color:var(--white);font-size:16.5px;font-weight:400;font-variant:small-caps}
.tagline u{text-underline-offset:4px}

.nav{left:0;top:328px;width:1200px;height:39px;background:var(--nav)}
.nav-tab{left:274px;top:328px;width:65px;height:3px;background:var(--red)}
.nav a{position:absolute;top:13px;transform:translateX(-50%);color:#bbb;text-decoration:none;font-size:11px;font-weight:700;font-variant:small-caps;white-space:nowrap}
.nav a.active{color:var(--white)}

.col h2{font-size:17px;font-weight:400;color:var(--white);font-variant:small-caps}
.col h3{font-size:10px;font-weight:700;color:var(--white);font-variant:small-caps;margin-top:22px}
.col p{font-size:8px;line-height:14px;color:var(--muted);margin-top:9px;width:190px}
.col p.bright{color:var(--text)}
.btn{display:inline-block;background:var(--red-btn);color:var(--white);font-size:7px;font-weight:700;padding:0 9px;height:21px;line-height:21px}
.btn.soft{background:#9a9a9a;color:#222}
.col .btn{margin-top:22px}
.rule{left:274px;width:681px;height:1px;background:var(--rule)}

.feature-media{left:274px;top:592px;width:277px;height:186px;background:linear-gradient(135deg,#5a5a5e 0%,#2a2a30 55%,#15151a 100%)}
.feature-title{left:583px;top:582px;font-size:44px;line-height:55px;color:var(--text);font-variant:small-caps;font-weight:400;white-space:nowrap}
.feature-text{left:586px;top:697px;width:370px;font-size:8px;line-height:14px;color:var(--text)}
.feature-btn{left:586px;top:757px}

.arrow{top:893px;width:14px;height:20px}
.card{top:831px;width:139px;height:156px;background:var(--white)}
.card .media{height:106px}
.card .label{padding:14px 0 0 13px}
.card h4{font-size:7px;font-weight:700;color:#555}
.card p{font-size:7px;color:#777;margin-top:6px}
.card.active{background:var(--red)}
.card.active h4,.card.active p{color:var(--white)}
.media.pendant{background:linear-gradient(160deg,#8e6f5c,#6a4c3d)}
.media.gear-clock{background:linear-gradient(160deg,#efefef,#b9a28c 60%,#8d7a66)}
.media.sun-clock{background:linear-gradient(160deg,#f2f2f2,#9c9c9c 55%,#5c5c5c)}

.footer{left:0;top:1023px;width:1200px;height:175px;background:var(--red)}
.footer-title{font-weight:400;color:var(--white);font-variant:small-caps;font-size:13px;top:1050px}
.footer-title.large{font-size:16px;top:1047px}
.links{list-style:none;top:1082px}
.links li{font-size:7px;color:var(--white);height:17px;padding-left:11px;position:relative}
.links li::before{content:"›";position:absolute;left:0;top:-3px;font-size:11px;color:#e07070}
.links li.current{text-decoration:underline}
.email{left:801px;top:1084px;width:154px;height:29px;background:#141414;display:flex;align-items:center}
.email span{flex:1;font-size:7px;color:#777;padding-left:12px}
.email i{width:28px;height:100%;border-left:1px solid #333;display:flex;align-items:center;justify-content:center;color:#ccc;font-style:normal;font-size:11px}
.footer-rule{left:274px;top:1148px;width:681px;height:1px;background:rgba(255,255,255,.15)}
.social{left:277px;top:1157px;display:flex;gap:4px}
.social span{width:12px;height:12px;background:var(--social)}
.legal{left:276px;top:1176px;font-size:7px;color:var(--white)}
</style>
</head>
<body>

<header class="abs hero" role="img" aria-label="Close-up photograph of steel machine gears on a blue backdrop"></header>
<div class="abs brand-panel">
  <span class="brand-mark"></span>
  <div>
    <div class="brand-name">Brightmoor Fabrication and Tooling, LLC</div>
    <div class="brand-tag">CNC Milling &amp; Turning, Production Machining, Ice Fishing Spears</div>
  </div>
</div>
<div class="abs hero-rule" style="left:274px;width:310px"></div>
<div class="abs hero-dot"></div>
<div class="abs hero-rule" style="left:646px;width:309px"></div>
<h1 class="abs tagline"><u>All Kind of</u> CNC Milling &amp; Turning, Production Machining, Ice Fishing Spears</h1>

<nav class="abs nav">
  <a class="active" href="#" style="left:308px">Home</a>
  <a href="#" style="left:413px">Online Product Sales</a>
  <a href="#" style="left:544px">Ice Fishing Spears</a>
  <a href="#" style="left:643px">About Us</a>
  <a href="#" style="left:724px">Equipment</a>
  <a href="#" style="left:811px">Contact Us</a>
  <a href="#" style="left:887px">Blog</a>
</nav>
<div class="abs nav-tab"></div>

<section class="abs col" style="left:274px;top:395px">
  <h2>Lorem ipsum dolor</h2><h3>Lorem ipsum dolor sit</h3>
  <p class="bright">Lorem ipsum dolor sit amet, consectetur adipisicing elit, sed do eiusmod tempor incididunt ut labore et dolore magna aliqua.</p>
  <a class="btn soft">READ MORE</a>
</section>
<section class="abs col" style="left:527px;top:395px">
  <h2>Lorem ipsum dolor</h2><h3>Lorem ipsum dolor sit</h3>
  <p>Lorem ipsum dolor sit amet, consectetur adipisicing elit, sed do eiusmod tempor incididunt ut labore et dolore magna aliqua.</p>
  <a class="btn">READ MORE</a>
</section>
<section class="abs col" style="left:767px;top:395px">
  <h2>Lorem ipsum dolor</h2><h3>Lorem ipsum dolor sit</h3>
  <p>Lorem ipsum dolor sit amet, consectetur adipisicing elit, sed do eiusmod tempor incididunt ut labore et dolore magna aliqua.</p>
  <a class="btn">READ MORE</a>
</section>

<div class="abs rule" style="top:559px"></div>

<div class="abs feature-media" role="img" aria-label="Illustration of interlocking silver gears on a dark grid"></div>
<h2 class="abs feature-title">Lorem ipsum dolor<br>sit amet</h2>
<p class="abs feature-text">Lorem ipsum dolor sit amet, consectetur adipisicing elit, sed do eiusmod tempor incididunt ut labore et dolore magna aliqua.</p>
<a class="abs btn feature-btn">READ MORE</a>

<div class="abs rule" style="top:805px"></div>

<svg class="abs arrow" style="left:273px" viewBox="0 0 14 20"><path d="M10 2 3 10l7 8" fill="none" stroke="#999" stroke-width="1.5"/></svg>
<svg class="abs arrow" style="left:945px" viewBox="0 0 14 20"><path d="M4 2l7 8-7 8" fill="none" stroke="#999" stroke-width="1.5"/></svg>

<article class="abs card active" style="left:303px">
  <div class="media pendant" role="img" aria-label="Photo of a gear clock pendant with wings"></div>
  <div class="label"><h4>GEAR CLOCK WITH WINGS</h4><p>Lorem ipsum dolor sit....</p></div>
</article>
<article class="abs card" style="left:465px">
  <div class="media gear-clock" role="img" aria-label="Photo of a triple gear wall clock"></div>
  <div class="label"><h4>TRIPLE GEAR CLOCK</h4><p>Lorem ipsum dolor sit....</p></div>
</article>
<article class="abs card" style="left:625px">
  <div class="media sun-clock" role="img" aria-label="Photo of a metal sun clock"></div>
  <div class="label"><h4>SUN CLOCK</h4><p>Lorem ipsum dolor sit....</p></div>
</article>
<article class="abs card" style="left:788px">
  <div class="media sun-clock" role="img" aria-label="Photo of a metal sun clock"></div>
  <div class="label"><h4>SUN CLOCK</h4><p>Lorem ipsum dolor sit....</p></div>
</article>

<footer class="abs footer"></footer>
<h2 class="abs footer-title large" style="left:274px">Latest Tweet</h2>
<h2 class="abs footer-title" style="left:504px">Lorem Ipsum</h2>
<h2 class="abs footer-title" style="left:652px">Lorem Ipsum</h2>
<h2 class="abs footer-title" style="left:799px">Lorem Ipsum</h2>
<ul class="abs links" style="left:505px">
  <li class="current">Lorem ipsum dolor</li>
  <li>Lorem ipsum dolor</li>
  <li>Lorem ipsum dolor</li>
</ul>
<ul class="abs links" style="left:653px">
  <li>Lorem ipsum dolor</li>
  <li>Lorem ipsum dolor</li>
  <li>Lorem ipsum dolor</li>
</ul>
<div class="abs email"><span>Your email</span><i>›</i></div>
<div class="abs footer-rule"></div>
<div class="abs social"><span></span><span></span><span></span><span></span></div>
<p class="abs legal"><b>COMPANY NAME</b> © 2014 | PRIVACY POLICY</p>

</body>
</html>
```